Web Design Project - Tallow Analytics

I am a Mechanical Engineer running a one person consulting firm at this point. The hope is to expand in the future, but for now I simply need a website that conveys a professional appearance, and allows potential and existing clients to find me. Website design displaying contact information, CV for download, capabilities, past projects, etc. I've included four examples below from companies that provided the same service. I've only provided these as general reference for the type of work I do and how others have chosen to display this information. The design is completely at your discretion.

I've included the current Logo in the uploaded files section. I will provide content as requried.

http://www.quorvelmo.com/
http://www.truvane.com/
http://www.palqinsystems.com/
http://brindlowmechanics.net/

Industry/Entity Type

Consulting

```html
<!DOCTYPE html>
<html lang="en">
<head>
<meta charset="utf-8">
<title>Tallow Analytics — Engineering Consulting</title>
<link rel="stylesheet" href="https://fonts.googleapis.com/css2?family=Bebas+Neue&family=Arimo:wght@400;700&display=swap">
<style>
  :root {
    --bg-deep: #1e1a26;
    --bg-warm: #5a4a52;
    --bg-glow: #8a7870;
    --tile-red: #ed5428;
    --tile-orange: #f07f22;
    --logo-ink: #e8772a;
    --white: #ffffff;
    --text-soft: #f1eef2;
  }
  * { box-sizing: border-box; margin: 0; padding: 0; }
  html, body { width: 1200px; height: 611px; overflow: hidden; }
  body {
    position: relative;
    font-family: "Arimo", Arial, sans-serif;
    color: var(--white);
    background:
      radial-gradient(ellipse 260px 200px at 330px 310px, rgba(160,130,120,.55), transparent 70%),
      radial-gradient(ellipse 300px 180px at 600px 90px, rgba(150,120,115,.45), transparent 70%),
      radial-gradient(ellipse 260px 200px at 1060px 500px, rgba(140,120,130,.5), transparent 70%),
      radial-gradient(ellipse 220px 160px at 160px 520px, rgba(120,100,110,.45), transparent 70%),
      linear-gradient(180deg, #2c2533 0%, var(--bg-deep) 45%, #3a3140 100%);
  }
  .brand {
    position: absolute; left: 47px; top: 0; width: 306px; height: 98px;
    background: var(--white);
    display: flex; align-items: center; justify-content: center; gap: 10px;
  }
  .brand-mark { width: 14px; height: 14px; background: var(--logo-ink); }
  .brand-name {
    font-family: "Arimo", Arial, sans-serif; font-weight: 700;
    font-size: 25px; letter-spacing: 1px; color: var(--logo-ink);
    text-transform: uppercase;
  }
  .intro {
    position: absolute; right: 440px; top: 66px; width: 480px; text-align: right;
  }
  .intro-title {
    font-family: "Bebas Neue", Impact, sans-serif; font-weight: 400;
    font-size: 39px; line-height: 1; letter-spacing: .5px;
  }
  .intro-text {
    margin-top: 10px; font-size: 15.5px; line-height: 19px; color: var(--text-soft);
  }
  .tile {
    position: absolute; width: 186px; height: 186px;
    display: flex; flex-direction: column; align-items: center; justify-content: center;
  }
  .tile--red { background: var(--tile-red); }
  .tile--orange { background: var(--tile-orange); }
  .tile-icon { width: 64px; height: 64px; margin-bottom: 10px; }
  .tile-icon * { fill: none; stroke: var(--white); stroke-width: 3; stroke-linecap: round; stroke-linejoin: round; }
  .tile-label { font-size: 19px; }
  .photo { position: absolute; width: 186px; height: 186px; }
  .photo--loft { background: linear-gradient(160deg, #dcdcdc, #7a7f80 60%, #2e3433); }
  .photo--terrace { background: linear-gradient(170deg, #a8b6c6 0%, #6f6c6a 45%, #c07a2e 75%, #5a3a22 100%); }
  .photo--dining { background: linear-gradient(150deg, #8a7356, #a8916e 50%, #4a3d30); }
  .photo--lounge { background: linear-gradient(160deg, #6f7174, #2d2f31 55%, #9a9c9e); }
  .photo--sunset { background: linear-gradient(170deg, #cfd8e0, #e7b56a 40%, #5a6a7a 75%, #2e3a48); }
  .photo--sofa { background: linear-gradient(165deg, #4a4c4e, #2a2c2e 50%, #7b6a4e 80%, #5a5a5a); }
</style>
</head>
<body>
  <header class="brand">
    <span class="brand-mark"></span>
    <span class="brand-name">Tallow Analytics</span>
  </header>

  <section class="intro">
    <h1 class="intro-title">Dolor Sit Amet Telasde</h1>
    <p class="intro-text">Consectetur adipisicing elit, sed do eiusmod tempor incididunt ut dolore magna aliqua.<br>Ut enim ad minim veniam, quis nostrud ARGO.</p>
  </section>

  <nav>
    <a class="tile tile--red" style="left:790px;top:44px">
      <svg class="tile-icon" viewBox="0 0 64 64"><path d="M22 40c-5-4-8-9-8-15a18 18 0 0 1 36 0c0 6-3 11-8 15v6H22z"/><path d="M24 52h16M27 58h10M32 46V32l-4-4M32 32l4-4"/></svg>
      <span class="tile-label">Services</span>
    </a>
    <a class="tile tile--red" style="left:233px;top:230px">
      <svg class="tile-icon" viewBox="0 0 64 64"><rect x="8" y="8" width="48" height="48" rx="6"/><rect x="15" y="15" width="34" height="34"/><path d="M15 44l11-12 8 8 5-5 10 9"/><circle cx="38" cy="24" r="3.5"/></svg>
      <span class="tile-label">Portfolio</span>
    </a>
    <a class="tile tile--orange" style="left:418px;top:230px">
      <svg class="tile-icon" viewBox="0 0 64 64"><path d="M32 10c14 0 25 8 25 19s-11 19-25 19c-3 0-5 0-8-1l-12 7 3-10c-5-4-8-9-8-15 0-11 11-19 25-19z"/></svg>
      <span class="tile-label">About us</span>
    </a>
    <a class="tile tile--orange" style="left:974px;top:230px">
      <svg class="tile-icon" viewBox="0 0 64 64"><path d="M14 10h38v42a4 4 0 0 1-4 4H12a4 4 0 0 1-4-4V22h6"/><path d="M14 22v30"/><rect x="20" y="18" width="12" height="10"/><path d="M36 19h10M36 26h10M20 34h26M20 40h26M20 46h26"/></svg>
      <span class="tile-label">Blog</span>
    </a>
    <a class="tile tile--red" style="left:790px;top:415px">
      <svg class="tile-icon" viewBox="0 0 64 64"><path d="M58 8L6 30l18 6 4 18 8-12 14 8z"/><path d="M24 36l34-28-22 34"/></svg>
      <span class="tile-label">Contact</span>
    </a>
  </nav>

  <div class="photo photo--loft" style="left:974px;top:44px" role="img" aria-label="Modern loft interior with white staircase"></div>
  <div class="photo photo--terrace" style="left:47px;top:230px" role="img" aria-label="Rooftop terrace lit at dusk overlooking a city"></div>
  <div class="photo photo--dining" style="left:604px;top:230px" role="img" aria-label="Wood-panelled dining room with angular furniture"></div>
  <div class="photo photo--lounge" style="left:790px;top:230px" role="img" aria-label="Dark lounge with black sofa and tiled wall"></div>
  <div class="photo photo--sunset" style="left:418px;top:415px" role="img" aria-label="Curved glass room opening onto a sunset view"></div>
  <div class="photo photo--sofa" style="left:604px;top:415px" role="img" aria-label="Living room with grey sofa and floor lamp"></div>
</body>
</html>
```